Startup photography business has a new logo, now we need business cards

Design a business card for the two partners of our business.
Our business Brisk Pelican has a new logo and we need to design a business card to showcase it and us.
Our colours of blue and orange are punchy and vivid, but how can we make the most of it on our card?

It should have our name Brisk Pelican
name of partner
phone number
email
website

Industry/Entity Type

Professional Photography

Contact Information for Business Card

Tom Ashworth
+61 400 55 61 72
tom@briskpelican.com.au
briskpelican.com.au

second card
Neil Porter
+61 400 918 263
neil@briskpelican.com.au
briskpelican.com.au

Colors
f37122
f68d4c
33a6d7
0592cd

Requirements
Must have
• one version of our logo, we have included options
• Name
• phone number
• email
• website
Nice to have
• instagram briskpelicanmedia
• twitter briskpelicanmedia
• facebook briskpelicanmedia

```html
<!DOCTYPE html>
<html lang="en">
<head>
<meta charset="utf-8">
<title>Brisk Pelican – Business Card</title>
<link rel="stylesheet" href="https://fonts.googleapis.com/css2?family=Open+Sans:wght@400;600;700;800&display=swap">
<style>
  :root {
    --backdrop: #2b2b2b;
    --card: #050505;
    --orange: #f37122;
    --orange-soft: #f68d4c;
    --blue: #33a6d7;
    --blue-deep: #0592cd;
    --white: #f4f4f4;
  }
  * { margin: 0; padding: 0; box-sizing: border-box; }
  html, body {
    width: 1200px; height: 900px; overflow: hidden;
    background: var(--backdrop);
    font-family: "Open Sans", Arial, sans-serif;
  }
  .canvas {
    width: 1200px; height: 900px;
    display: flex; flex-direction: column; align-items: center; justify-content: center;
    gap: 36px;
  }
  .card {
    position: relative;
    width: 700px; height: 400px;
    background: var(--card);
    border-radius: 22px;
    overflow: hidden;
  }

  /* Front */
  .card-front { display: flex; flex-direction: column; align-items: center; justify-content: center; }
  .brand {
    display: flex; align-items: center; gap: 14px;
  }
  .brand-dot {
    border-radius: 50%;
    background: var(--orange);
  }
  .brand-name {
    color: var(--blue);
    font-weight: 800;
    text-transform: uppercase;
    letter-spacing: 1px;
  }
  .card-front .brand-dot { width: 46px; height: 46px; }
  .card-front .brand-name { font-size: 46px; }
  .social-handle {
    margin-top: 22px;
    color: var(--white);
    font-size: 17px;
    font-weight: 400;
  }

  /* Back */
  .card-back .brand {
    position: absolute; left: 40px; top: 60px;
  }
  .card-back .brand-dot { width: 30px; height: 30px; }
  .card-back .brand-name { font-size: 32px; }

  .person-name {
    position: absolute; right: 40px; top: 198px;
    font-size: 30px; font-weight: 800; text-transform: uppercase; letter-spacing: .5px;
  }
  .person-name .first { color: var(--orange); }
  .person-name .last { color: var(--blue); }

  .divider {
    position: absolute; left: 0; right: 40px; top: 246px;
    height: 2px; background: var(--blue-deep);
  }
  .contact-list {
    position: absolute; right: 40px; top: 260px;
    list-style: none; text-align: right;
  }
  .contact-list li {
    display: flex; align-items: center; justify-content: flex-end; gap: 10px;
    color: var(--blue);
    font-size: 17px; line-height: 28px; font-weight: 400;
  }
  .contact-list svg { width: 15px; height: 15px; flex: none; }
</style>
</head>
<body>
<main class="canvas">

  <section class="card card-front">
    <div class="brand">
      <span class="brand-dot"></span>
      <span class="brand-name">Brisk Pelican</span>
    </div>
    <p class="social-handle">briskpelicanmedia</p>
  </section>

  <section class="card card-back">
    <div class="brand">
      <span class="brand-dot"></span>
      <span class="brand-name">Brisk Pelican</span>
    </div>

    <h1 class="person-name"><span class="first">Tom</span> <span class="last">Ashworth</span></h1>
    <div class="divider"></div>

    <ul class="contact-list">
      <li>+61 400 55 61 72
        <svg viewBox="0 0 16 16" aria-hidden="true"><path d="M4 1.5l2.2 3-1.4 1.6c.8 1.8 2.3 3.3 4.1 4.1l1.6-1.4 3 2.2-1.2 2.5C7 13.2 2.8 9 2.3 3.7z" fill="none" stroke="var(--orange)" stroke-width="1.4" stroke-linejoin="round"/></svg>
      </li>
      <li>tom@briskpelican.com.au
        <svg viewBox="0 0 16 16" aria-hidden="true"><rect x="1.5" y="3.5" width="13" height="9" rx="1" fill="none" stroke="var(--orange)" stroke-width="1.4"/><path d="M1.5 4l6.5 5 6.5-5" fill="none" stroke="var(--orange)" stroke-width="1.4"/></svg>
      </li>
      <li>www.briskpelican.com.au
        <svg viewBox="0 0 16 16" aria-hidden="true"><circle cx="8" cy="8" r="6.3" fill="none" stroke="var(--orange)" stroke-width="1.4"/><ellipse cx="8" cy="8" rx="2.8" ry="6.3" fill="none" stroke="var(--orange)" stroke-width="1.2"/><path d="M1.7 8h12.6" stroke="var(--orange)" stroke-width="1.2"/></svg>
      </li>
    </ul>
  </section>

</main>
</body>
</html>
```